Bookkeeping website design

We need a basic site design for wordpress.
We are a bookkeeping business and will need to present a look consistent with the colours and style of the logo.

Target Market(s)

Business owners

Industry/Entity Type

Accounting/Bookkeeping

Coding

Coded - Design and coding required

Number of Pages Required

1 page

```html
<!DOCTYPE html>
<html lang="en">
<head>
<meta charset="utf-8">
<title>Ledgerly Bookkeeping</title>
<link href="https://fonts.googleapis.com/css2?family=Bebas+Neue&family=Poppins:wght@400;500;600&display=swap" rel="stylesheet">
<style>
:root{
  --green:#8cc63f;
  --teal:#2cc6b4;
  --cyan:#1ec8e8;
  --ink:#111;
  --body:#666;
  --footer:#070707;
  --grad:linear-gradient(90deg,#8cc63f,#1ec8e8);
}
*{margin:0;padding:0;box-sizing:border-box}
html,body{width:1200px;height:3548px;overflow:hidden}
body{position:relative;font-family:'Poppins',sans-serif;color:var(--ink);background:#fff}
.abs{position:absolute}
.btn{position:absolute;display:flex;align-items:center;justify-content:center;background:var(--grad);color:#fff;font-weight:500;font-size:15px;border-radius:7px;text-transform:uppercase}
.label{position:absolute;color:var(--teal);font-weight:500;font-size:14px}
.heading{position:absolute;font-weight:500;font-size:30px;text-transform:uppercase;letter-spacing:.3px}

/* hero */
.hero{position:absolute;left:0;top:0;width:1200px;height:712px;background:linear-gradient(100deg,#2c3a44 0%,#3d4a52 40%,#4a4038 65%,#1c2024 100%)}
.brand{position:absolute;display:flex;align-items:center;gap:10px;font-weight:600;font-size:24px;color:var(--green)}
.brand i{display:block;width:22px;height:22px;background:var(--cyan)}
.topbar{position:absolute;right:63px;top:8px;display:flex;align-items:center;gap:10px;color:#fff;font-size:15px;font-weight:500}
.topbar span.login{font-size:13px;font-weight:400}
.navband{position:absolute;left:435px;top:34px;width:765px;height:40px;background:linear-gradient(90deg,rgba(30,200,232,.55),rgba(140,198,63,.55));clip-path:polygon(0 0,100% 0,100% 100%,28px 100%)}
.nav{position:absolute;right:63px;top:34px;height:40px;display:flex;gap:22px;align-items:center;font-size:12px;color:#fff}
.nav .on{position:relative}
.nav .on::after{content:"";position:absolute;left:0;right:0;bottom:-10px;height:2px;background:var(--teal)}
.hero h1{position:absolute;left:61px;top:262px;font-family:'Bebas Neue',sans-serif;font-weight:400;font-size:60px;line-height:58px;color:#fff}
.hero h2{position:absolute;left:61px;top:380px;font-weight:500;font-size:26px;color:var(--green)}
.hero p{position:absolute;left:61px;top:420px;width:360px;font-size:12px;line-height:19px;color:#fff}
.scroll{position:absolute;left:1126px;top:428px;font-size:11px;color:#fff;writing-mode:vertical-rl;transform:rotate(180deg)}
.scroll-line{position:absolute;left:1133px;top:510px;width:1px;height:84px;background:rgba(255,255,255,.5)}

/* about */
.about-photo{position:absolute;left:167px;top:788px;width:374px;height:374px;background:linear-gradient(135deg,#c9ced2,#8a8a86 60%,#6a4a32)}
.about-text{position:absolute;left:607px;top:881px;width:400px;font-size:11.5px;line-height:19.5px;color:var(--body)}
.about-text p{margin-bottom:12px}

/* services */
.services{position:absolute;left:0;top:1246px;width:1200px;height:532px;background:linear-gradient(90deg,#eaf7f8,#f7f9ee)}
.card{position:absolute;top:173px;width:299px;height:284px}
.card .cap{position:absolute;left:16px;bottom:22px;color:#fff}
.card b{display:block;font-weight:500;font-size:16px;margin-bottom:2px}
.card small{font-size:11.5px}
.card .go{position:absolute;right:14px;bottom:24px;width:32px;height:32px;border-radius:50%;background:var(--grad)}

/* benefits */
.benefit{position:absolute;width:330px}
.benefit .ico{position:absolute;left:0;top:0;width:66px;height:66px;border-radius:8px;background:#fff;box-shadow:0 2px 10px rgba(0,0,0,.1)}
.benefit h3{position:absolute;left:86px;top:4px;font-size:15px;font-weight:500;white-space:nowrap}
.benefit p{position:absolute;left:86px;top:30px;width:220px;font-size:11.5px;line-height:19px;color:var(--body)}
.person{position:absolute;left:737px;top:1902px;width:386px;height:413px;background:radial-gradient(ellipse at 55% 55%,#8d8f93 0%,#6a6d72 45%,rgba(255,255,255,0) 72%)}

/* testimonials */
.testi{position:absolute;left:0;top:2315px;width:1200px;height:486px;background:linear-gradient(90deg,#1ec8e8 0%,#4ec2a0 45%,#8cc63f 100%)}
.testi .label,.testi .heading{left:0;width:1200px;text-align:center}
.testi .label{color:#fff}
.avatar{position:absolute;left:554px;top:166px;width:92px;height:92px;border-radius:50%;border:3px solid #fff;background:linear-gradient(160deg,#5a3a2a,#a0705a)}
.arrow{position:absolute;top:251px;width:38px;height:38px;border-radius:50%;border:1.5px solid #fff}
.quote{position:absolute;left:320px;top:292px;width:560px;text-align:center;color:#fff;font-size:12.5px;line-height:22.5px}
.client{position:absolute;left:0;width:1200px;top:404px;text-align:center;color:#fff;font-size:15px;font-weight:500}

/* get started */
.start{position:absolute;left:0;top:2801px;width:1200px;height:426px;background:linear-gradient(180deg,#fff 0%,#fff 45%,#ececec 100%)}
.field{position:absolute;left:357px;width:486px;height:40px;border:1px solid #ddd;border-radius:8px;background:#fff;font-size:11px;color:#777;padding:13px 17px}

/* footer */
.footer{position:absolute;left:0;top:3227px;width:1200px;height:321px;background:var(--footer);color:#fff}
.fcol{position:absolute;top:50px}
.fcol h4{color:var(--teal);font-weight:500;font-size:15px;margin-bottom:14px}
.fcol ul{list-style:none;font-size:11.5px}
.fcol li{height:24px;padding-left:19px;position:relative}
.fcol li::before{content:"";position:absolute;left:0;top:5px;width:5px;height:5px;border:1.5px solid var(--teal);border-radius:50%}
.social{position:absolute;top:3422px;width:38px;height:38px;border-radius:50%;background:var(--grad)}
.copy{position:absolute;left:61px;top:3508px;width:1078px;height:40px;background:var(--grad);clip-path:polygon(0 0,100% 0,97% 100%,3% 100%);color:#fff;font-size:11px;display:flex;align-items:center;justify-content:center}
</style>
</head>
<body>

<!-- Hero -->
<section class="hero" role="img" aria-label="Photo of a woman on the phone working at a laptop with paperwork">
</section>
<div class="brand" style="left:61px;top:32px"><i></i>Ledgerly</div>
<div class="navband"></div>
<div class="topbar">
  <svg width="18" height="18" viewBox="0 0 24 24"><path d="M6.6 10.8a15 15 0 0 0 6.6 6.6l2.2-2.2c.3-.3.7-.4 1-.2 1.1.4 2.3.6 3.6.6.6 0 1 .4 1 1V20c0 .6-.4 1-1 1A17 17 0 0 1 3 4c0-.6.4-1 1-1h3.5c.6 0 1 .4 1 1 0 1.3.2 2.5.6 3.6.1.3 0 .7-.2 1z" fill="#8cc63f"/></svg>
  <span>555 010 2040</span>
  <svg width="16" height="16" viewBox="0 0 24 24" fill="none" stroke="#2cc6b4" stroke-width="2"><circle cx="12" cy="12" r="10"/><circle cx="12" cy="10" r="3"/><path d="M6 19c2-3 10-3 12 0"/></svg>
  <span class="login">Login</span>
</div>
<nav class="nav">
  <span class="on">Home</span><span>About</span><span>Services</span><span>Benefits</span><span>Testimonials</span><span>Contact Us</span>
</nav>
<h1 class="hero-title" style="position:absolute;left:61px;top:262px;font-family:'Bebas Neue',sans-serif;font-weight:400;font-size:60px;line-height:58px;color:#fff">YOU RUN YOUR<br>BUSINESS.</h1>
<h2 style="position:absolute;left:61px;top:380px;font-weight:500;font-size:26px;color:var(--green)">We'll Handle Your Finance.</h2>
<p style="position:absolute;left:61px;top:421px;width:360px;font-size:12px;line-height:19px;color:#fff">From bookkeeping to tax filling, Ledgerly is the all-in-one finacial toolkit your business can count on.</p>
<div class="btn" style="left:61px;top:475px;width:133px;height:39px">Get Started</div>
<div class="scroll">Scroll Down</div>
<div class="scroll-line"></div>

<!-- About -->
<div class="about-photo" role="img" aria-label="Photo of a woman using a calculator over financial documents"></div>
<div class="label" style="left:607px;top:794px">About Us</div>
<div class="heading" style="left:605px;top:824px">Ledgerly Bookkeeping</div>
<div class="about-text">
  <p>Lorem Ipsum has been the industry's standard dummy text ever since the 1500s, when an unknown printer took a galley of typescrambled it to make a type specimen book. It has survived not.</p>
  <p>Lorem Ipsum has been the industry's standard dummy text ever since the 1500s, when an unknown printer took a galley of type and scrambled it to make a type specimen book. It has survived not only five centuries, but also the leap into electronic typesetting, remaining essentially unchanged.</p>
  <p>Lorem Ipsum has been the industry's standard dummy text ever since the, when an unknown printer took a galley of type.</p>
</div>
<div class="btn" style="left:606px;top:1113px;width:134px;height:40px">Learn More</div>

<!-- Services -->
<section class="services">
  <div class="label" style="left:60px;top:75px">We Are Expert In</div>
  <div class="heading" style="left:61px;top:104px">Our Services</div>
  <div class="card" style="left:0;background:linear-gradient(160deg,#6a5a40,#3a3a3a)" role="img" aria-label="Photo of hands on a calculator">
    <div class="cap"><b>IncomeTax</b><small>Lorem Ipsum has been the industry.</small></div><div class="go"></div></div>
  <div class="card" style="left:300px;background:linear-gradient(160deg,#d8d8d4,#3a3c40)" role="img" aria-label="Photo of a man reviewing a clipboard">
    <div class="cap"><b>Financial Audit</b><small>Lorem Ipsum has been the industry.</small></div><div class="go"></div></div>
  <div class="card" style="left:600px;background:linear-gradient(160deg,#c8c8c6,#4a4a48)" role="img" aria-label="Photo of a laptop showing a stock chart">
    <div class="cap"><b>Outsourced CFO</b><small>Lorem Ipsum has been the industry.</small></div><div class="go"></div></div>
  <div class="card" style="left:900px;background:linear-gradient(160deg,#2a3040,#9aa0a8)" role="img" aria-label="Photo of a hand writing on a business report">
    <div class="cap"><b>Business Valuation</b><small>Lorem Ipsum has been the industry.</small></div><div class="go"></div></div>
</section>

<!-- Benefits -->
<div class="label" style="left:0;width:1200px;text-align:center;top:1853px">Why Us</div>
<div class="heading" style="left:0;width:1200px;text-align:center;top:1877px">Benefits</div>
<div class="benefit" style="left:61px;top:2006px"><div class="ico"></div><h3>No Stress Tax Season</h3><p>Lorem Ipsum has been the industry standard dummy text ever.</p></div>
<div class="benefit" style="left:388px;top:2006px"><div class="ico"></div><h3>Monthly Payment Handled</h3><p>Lorem Ipsum has been the industry standard dummy text ever.</p></div>
<div class="benefit" style="left:61px;top:2144px"><div class="ico"></div><h3>Know Your Financial</h3><p>Lorem Ipsum has been the industry standard dummy text ever.</p></div>
<div class="benefit" style="left:388px;top:2144px"><div class="ico"></div><h3>Accurate &amp; Effective Bookkeeping</h3><p>Lorem Ipsum has been the industry standard dummy text ever.</p></div>
<div class="person" role="img" aria-label="Photo of a surprised young man holding a laptop"></div>

<!-- Testimonials -->
<section class="testi" role="group" aria-label="Testimonials">
  <div class="label" style="top:79px">Testimonials</div>
  <div class="heading" style="top:104px">What Our Client Say</div>
  <div class="avatar" role="img" aria-label="Client portrait photo"></div>
  <svg class="arrow" style="left:190px" viewBox="0 0 38 38"><path d="M21 12l-7 7 7 7" fill="none" stroke="#fff" stroke-width="1.5"/></svg>
  <svg class="arrow" style="left:971px" viewBox="0 0 38 38"><path d="M17 12l7 7-7 7" fill="none" stroke="#fff" stroke-width="1.5"/></svg>
  <p class="quote">" Lorem Ipsum has been the industry's standard dummy text ever since the 1500s, when an unknown printer took a galley of type and scrambled it to make a type specimen book. It has survived not only five centuries, but also the leap into electronic typesetting, remaining essentially unchanged. "</p>
  <div class="client">&#8211; Client Name</div>
</section>

<!-- Get started -->
<section class="start">
  <div class="heading" style="left:0;width:1200px;text-align:center;top:72px">Get Started</div>
  <p style="position:absolute;left:380px;width:440px;top:126px;text-align:center;font-size:13px;line-height:21px;color:var(--body)">Join thousands of small business owners who trust Ledgerly with their bookkeeping.</p>
  <div class="field" style="top:204px">Enter Name *</div>
  <div class="field" style="top:255px">Enter Email *</div>
  <div class="btn" style="left:533px;top:310px;width:135px;height:39px">Get Started</div>
</section>

<!-- Footer -->
<footer class="footer">
  <div class="brand" style="left:61px;top:62px;font-size:30px"><i style="width:26px;height:26px"></i>Ledgerly</div>
  <p style="position:absolute;left:61px;top:146px;width:400px;font-size:11.5px;line-height:20px">Lorem Ipsum has been the industry's standard dummy text ever since the 1500s, when an unknown printer took a galley.</p>
  <div class="fcol" style="left:504px"><h4>SITEMAP</h4><ul><li>Home</li><li>About Us</li><li>Services</li><li>Work Gallery</li><li>News</li><li>Contact Us</li></ul></div>
  <div class="fcol" style="left:715px"><h4>SERVICES</h4><ul><li>Interlocking</li><li>Flagstone Installation</li><li>Repair Services</li><li>Install Sod</li></ul></div>
  <div class="fcol" style="left:925px"><h4>CONTACT US</h4></div>
  <svg class="abs" style="left:925px;top:87px" width="16" height="22" viewBox="0 0 16 22"><path d="M8 1a7 7 0 0 0-7 7c0 5 7 13 7 13s7-8 7-13a7 7 0 0 0-7-7z" fill="none" stroke="#8cc63f" stroke-width="2"/><circle cx="8" cy="8" r="2.5" fill="#1ec8e8"/></svg>
  <p class="abs" style="left:960px;top:84px;width:180px;font-size:11px;line-height:19.5px">Ledgerly<br><br>101 - Lorem ipsum simple text print type setting Industry.</p>
  <svg class="abs" style="left:925px;top:159px" width="18" height="18" viewBox="0 0 24 24"><path d="M6.6 10.8a15 15 0 0 0 6.6 6.6l2.2-2.2c.3-.3.7-.4 1-.2 1.1.4 2.3.6 3.6.6.6 0 1 .4 1 1V20c0 .6-.4 1-1 1A17 17 0 0 1 3 4c0-.6.4-1 1-1h3.5c.6 0 1 .4 1 1 0 1.3.2 2.5.6 3.6.1.3 0 .7-.2 1z" fill="#8cc63f"/></svg>
  <p class="abs" style="left:960px;top:159px;font-size:15px">555 010 2040</p>
  <svg class="abs" style="left:925px;top:197px" width="18" height="14" viewBox="0 0 18 14"><rect width="18" height="14" rx="2" fill="#2cc6b4"/><path d="M1 2l8 6 8-6" fill="none" stroke="#070707" stroke-width="1.5"/></svg>
  <p class="abs" style="left:960px;top:195px;font-size:11.5px">info@ledgerly.example</p>
</footer>
<div class="social" style="left:61px" aria-label="Social profile"></div>
<div class="social" style="left:105px" aria-label="Social profile"></div>
<div class="copy">&copy;MAPLE CREST STUDIO -2021 Allrights reserved.</div>

</body>
</html>
```